Events and Parties web-site needs a Web Design

VoTrel needs a web design.
VoTrel means The Bees in Italian.
VoTrel target market is people who is organizing parties and events.
Our mission is that the parties and events of our clients exceed their expectations by providing them web and mobile tools.
Our vision is to be the best and biggest party web portal of the country.
The main features of our web site is to let people invite guests and search suppliers/providers. Guests will also confirm presence (RSVP) and buy presents/gifts at the site as well.
Our slogan is "Curta sua festa desde já !" that means "Enjoy our party now !" in Brazilian Portuguese.
The idea here is that the party starts now and not only at the scheduled date and time.
Updates
It seems that must have and nice to have briefing is not appearing to you as I filled. So I will type it agai here:
Our slogan text that is "Curta sua festa desde já !" that means "Enjoy your party now !".
Space to paid ads.
Language switch to Spanish. Brazilian Portuguese is our default language.
Logon form with 2 inputs: Email and password.
RSVP form with 2 inputs: Event ID and password
Kendro trusted site seal (SSL/HTTPS) logo.
Update to my briefing: Only event organizer and guests will be able to see details of the events/parties like photos/blog, guest list and etc. Suppliers will be searched and rated like stayvoro.com/roamgliq.
Target Market(s)
VoTrel target market is amateur and professional people who are organizing parties and events.
Our mission is that the parties and events of our clients exceed their expectations by providing them easy and fast web and mobile tools.
Our vision is to be the best and biggest party portal of our country.
The main features of our web site is to let people invite guests and search suppliers/providers. Guests will also confirm presence (RSVP) and buy presents at the site.
Industry/Entity Type
Events
Requirements
Must have
- Design and colors compliant with attached logo.
- Our slogan text that is "Curta sua festa desde já !" that means "Enjoy your party now !".
- Space to paid ads.
- Language switch to Spanish. Brazilian Portuguese is our default language.
- Logon form with 2 inputs: Email and password.
- RSVP form with 2 inputs: Event ID and password
- Kendro trusted site seal (SSL/HTTPS) logo.
Nice to have
- VoTrel stands for The Bees in Italian. It would be very nice to have a not so explicit idea that each user is a bee and VoTrel is the hive where party/event occurs.
Should not have
- No PageMill please.
- No infant/child oriented designs please. Our market is not only children birthdays but also other parties and events like marriages, corporate events and so on

```html
<!DOCTYPE html>
<html lang="en">
<head>
<meta charset="utf-8">
<title>VoTrel – Start something</title>
<link rel="stylesheet" href="https://fonts.googleapis.com/css2?family=Lato:wght@300;400;700;900&family=Open+Sans:wght@400;700;800&family=Great+Vibes&display=swap">
<style>
  :root {
    --amber: #fbb414;
    --amber-deep: #f39a0b;
    --gold: #ffd13b;
    --brown: #2b0800;
    --brown-mid: #3a1205;
    --sky-top: #1d3fd0;
    --sky-mid: #3a72e4;
    --sky-low: #8fc0f0;
    --paper: #f8f8f8;
    --ink: #3a3a3a;
    --nav-grey: #777;
    --white: #ffffff;
    --social: #4a66a8;
  }
  * { box-sizing: border-box; margin: 0; padding: 0; }
  html, body { width: 1200px; height: 1044px; overflow: hidden; }
  body { position: relative; background: var(--paper); font-family: "Lato", sans-serif; color: var(--ink); }

  .site-header { position: absolute; left: 0; top: 0; width: 1200px; height: 129px; background: #f3f4f6; border-bottom: 1px solid #c9c9c9; }
  .brand { position: absolute; left: 550px; top: 78px; display: flex; align-items: center; gap: 8px; }
  .brand-dot { width: 18px; height: 18px; border-radius: 50%; background: var(--amber); }
  .brand-name { font-family: "Lato", sans-serif; font-weight: 400; font-size: 34px; color: var(--brown); line-height: 1; }
  .login-btn { position: absolute; left: 915px; top: 25px; width: 89px; height: 28px; background: var(--gold); border: 1px solid #e9b91d; border-radius: 2px; color: var(--white); font-weight: 700; font-size: 15px; text-align: center; line-height: 27px; }
  .main-nav { position: absolute; top: 99px; font-size: 15px; font-weight: 300; color: var(--nav-grey); display: flex; align-items: center; }
  .main-nav a { color: inherit; text-decoration: none; }
  .main-nav .sep { width: 1px; height: 16px; background: #aaa; margin: 0 12px; }
  .main-nav .current { color: var(--brown); font-weight: 400; }
  .nav-left { left: 199px; }
  .nav-right { left: 877px; }

  .hero { position: absolute; left: 0; top: 130px; width: 1200px; height: 673px; background: linear-gradient(180deg, var(--sky-top) 0%, var(--sky-mid) 55%, var(--sky-low) 100%); }
  .hero-sky { position: absolute; inset: 0; }
  .hero-title { position: absolute; left: 0; width: 1132px; top: 60px; text-align: center; font-family: "Great Vibes", cursive; font-size: 64px; font-weight: 400; color: var(--amber); line-height: 1; }
  .hero-sub { position: absolute; left: 400px; width: 310px; top: 115px; text-align: center; font-size: 16px; font-weight: 300; color: var(--white); line-height: 19px; }

  .browser { position: absolute; left: 279px; top: 184px; width: 563px; height: 338px; background: #fff; box-shadow: 0 2px 6px rgba(0,0,0,.35); overflow: hidden; }
  .browser-bar { height: 23px; background: linear-gradient(#eee, #d6d6d6); display: flex; align-items: center; padding-left: 8px; gap: 6px; }
  .browser-bar svg { flex: none; }
  .browser-url { flex: 1; height: 13px; margin-right: 4px; background: #fff; border: 1px solid #bbb; border-radius: 2px; }
  .browser-head { height: 41px; background: #fbeee6; display: flex; align-items: center; padding-left: 45px; gap: 34px; }
  .mini-brand { display: flex; align-items: center; gap: 4px; font-size: 11px; color: var(--brown); }
  .mini-brand i { width: 8px; height: 8px; border-radius: 50%; background: var(--amber); }
  .browser-head p { font-family: "Open Sans", sans-serif; font-size: 10px; letter-spacing: .4px; color: #444; }
  .browser-photo { height: 274px; background: linear-gradient(90deg, #3b2c24 0%, #c98a6a 35%, #e9b7a0 60%, #d95040 100%); }

  .phone { position: absolute; left: 759px; top: 230px; width: 151px; height: 324px; background: #111; border-radius: 20px; border: 2px solid #444; }
  .phone-screen { position: absolute; left: 8px; top: 45px; width: 133px; height: 234px; background: linear-gradient(180deg, #f0d860 0%, #e8c9a8 45%, #d8cfc0 100%); }
  .phone-brand { position: absolute; left: 36px; top: 72px; display: flex; align-items: center; gap: 4px; font-size: 17px; color: var(--brown); }
  .phone-brand i { width: 10px; height: 10px; border-radius: 50%; background: var(--amber); }
  .download-btn { position: absolute; left: 13px; top: 161px; width: 109px; height: 22px; background: var(--amber-deep); border: 1px solid #c36c00; border-radius: 2px; color: var(--white); font-weight: 700; font-size: 12px; text-align: center; line-height: 20px; }
  .phone-home { position: absolute; left: 61px; top: 289px; width: 25px; height: 25px; border-radius: 50%; border: 2px solid #444; }

  .signup { position: absolute; left: 197px; top: 716px; width: 806px; height: 142px; }
  .signup-bg { position: absolute; inset: 0; }
  .signup-title { position: absolute; left: 0; width: 806px; top: 22px; text-align: center; font-family: "Open Sans", sans-serif; font-weight: 800; font-size: 19px; color: var(--brown); text-shadow: 0 0 2px #fff, 0 0 2px #fff; }
  .field { position: absolute; top: 57px; height: 23px; background: #fff; border: 1px solid #e1a40c; font-family: "Open Sans", sans-serif; font-size: 9px; color: #999; line-height: 21px; padding-left: 6px; }
  .or { position: absolute; left: 567px; top: 57px; font-weight: 700; font-size: 17px; color: var(--white); }
  .social-btn { position: absolute; left: 606px; top: 57px; width: 158px; height: 22px; background: var(--social); border: 1px solid #34508c; border-radius: 2px; color: var(--white); font-size: 11px; font-weight: 300; display: flex; align-items: center; }
  .social-btn i { width: 22px; height: 20px; border-right: 1px solid #34508c; display: flex; align-items: center; justify-content: center; }
  .social-btn i::before { content: ""; width: 7px; height: 7px; background: #fff; }
  .social-btn span { flex: 1; text-align: center; }
  .signup-btn { position: absolute; left: 311px; top: 97px; width: 184px; height: 29px; background: var(--brown-mid); border: 1px solid #f6d48a; border-radius: 2px; color: var(--white); font-size: 13px; font-weight: 300; text-align: center; line-height: 27px; }

  .welcome { position: absolute; left: 205px; top: 873px; width: 790px; text-align: center; }
  .welcome h2 { font-family: "Open Sans", sans-serif; font-weight: 800; font-size: 30px; color: var(--amber); text-shadow: -1px -1px 0 var(--brown), 1px -1px 0 var(--brown), -1px 1px 0 var(--brown), 1px 1px 0 var(--brown); line-height: 38px; }
  .welcome p { margin-top: 17px; font-family: "Open Sans", sans-serif; font-size: 10.2px; line-height: 12.7px; color: #444; }

  .site-footer { position: absolute; left: 0; top: 1014px; width: 1200px; height: 30px; background: var(--brown); color: var(--white); font-size: 10px; font-weight: 700; text-align: center; line-height: 30px; }
</style>
</head>
<body>
  <header class="site-header">
    <nav class="main-nav nav-left">
      <a class="current" href="#">Home</a><span class="sep"></span><a href="#">How it Works</a>
    </nav>
    <div class="brand"><span class="brand-dot"></span><span class="brand-name">VoTrel</span></div>
    <nav class="main-nav nav-right">
      <a href="#">Features</a><span class="sep"></span><a href="#">Pricing</a>
    </nav>
    <a class="login-btn">LOGIN</a>
  </header>

  <section class="hero">
    <div class="hero-sky" role="img" aria-label="Blue sky with white clouds and floating purple, yellow and blue party balloons"></div>
    <h1 class="hero-title">Start something</h1>
    <p class="hero-sub">Lorem ipsum dolor sit amet, consectetuer adipiscing elit,</p>

    <div class="browser">
      <div class="browser-bar">
        <svg width="26" height="10" viewBox="0 0 26 10"><path d="M10 5H2M5 2L2 5l3 3M16 5h8M21 2l3 3-3 3" stroke="#888" stroke-width="1.5" fill="none"/></svg>
        <div class="browser-url"></div>
      </div>
      <div class="browser-head">
        <span class="mini-brand"><i></i>VoTrel</span>
        <p>Lorem ipsum dolor sit amet, consectetuer adipiscing elit,</p>
      </div>
      <div class="browser-photo" role="img" aria-label="Photo of a businessman in a suit beside a family celebrating a birthday with a cake"></div>
    </div>

    <div class="phone">
      <div class="phone-screen" role="img" aria-label="Photo of a child in a party hat on the app screen">
        <span class="phone-brand"><i></i>VoTrel</span>
        <a class="download-btn">Download Now!</a>
      </div>
      <div class="phone-home"></div>
    </div>
  </section>

  <section class="signup">
    <svg class="signup-bg" width="806" height="142" viewBox="0 0 806 142" preserveAspectRatio="none">
      <path d="M0 22 Q403 -22 806 22 V142 H0 Z" fill="#fbb414"/>
    </svg>
    <h3 class="signup-title">ENJOY OUR PARTY NOW !</h3>
    <div class="field" style="left:42px;width:159px;">Full Name</div>
    <div class="field" style="left:222px;width:158px;">E-mail</div>
    <div class="field" style="left:396px;width:158px;">Password</div>
    <span class="or">OR</span>
    <a class="social-btn"><i></i><span>Sign up with Friendo</span></a>
    <a class="signup-btn">Sign up. It's free!</a>
  </section>

  <section class="welcome">
    <h2>WELCOME</h2>
    <p>Lorem ipsum dolor sit amet, consectetuer adipiscing elit, sed diam nonummy nibh euismod tincidunt ut laoreet dolore magna aliquam erat volutpat. Ut wisi enim ad minim veniam, quis nostrud exerci tation ullamcorper suscipit lobortis nisl ut aliquip ex ea commodo consequat. Duis autem vel eum iriure dolor in hendrerit in vulputate velit esse molestie consequat, vel illum dolore eu feugiat nulla facilisis at vero eros et accumsan et iusto odio dignissim qui blandit praesent luptatum zzril delenit augue duis dolore te feugait nulla facilisi.</p>
  </section>

  <footer class="site-footer">© 2014 VoTrel.com</footer>
</body>
</html>
```